Ceiling fan flyer design

We are after a double sided flyer design offering ceiling fan installations

Target Market(s)

Home owners

Requirements
Must have
• content listed

```html
<!DOCTYPE html>
<html lang="en">
<head>
<meta charset="utf-8">
<title>Ceiling Fan Flyer</title>
<link href="https://fonts.googleapis.com/css2?family=Roboto:ital,wght@0,400;0,700;1,300;1,400;1,700;1,900&display=swap" rel="stylesheet">
<style>
  :root{
    --teal:#12a0a6;
    --teal-dark:#0b7f86;
    --teal-light:#35c3c9;
    --orange:#f07a2c;
    --orange-deep:#d9622b;
    --orange-soft:#f9b24a;
    --grey:#8a8d90;
    --grey-light:#c9cbcd;
    --ink:#333;
    --white:#fff;
  }
  *{margin:0;padding:0;box-sizing:border-box}
  html,body{width:1200px;height:900px;overflow:hidden;background:var(--white);font-family:"Roboto",Arial,sans-serif}
  .canvas{position:relative;width:1200px;height:900px}
  .page{position:absolute;top:38px;width:581px;height:824px;overflow:hidden}
  .page--front{left:15px;background:var(--teal)}
  .page--back{left:603px;background:linear-gradient(180deg,var(--teal-dark) 0%,var(--teal-light) 45%,var(--teal) 100%)}
  .page svg.shapes{position:absolute;inset:0}
  .abs{position:absolute}

  /* front */
  .front-title{left:45px;top:34px;color:var(--white);font-style:italic;line-height:1}
  .front-title .light{font-weight:300;font-size:50px;display:block}
  .front-title .bold{font-weight:700;font-size:52px;display:block;margin-top:4px}
  .brand{font-weight:700;font-style:normal;color:var(--orange-deep);font-size:17px;line-height:1.1;display:flex;align-items:center;gap:6px}
  .brand .dot{width:18px;height:18px;border-radius:50%;background:var(--orange)}
  .front-brand{left:404px;top:430px;width:150px}
  .offer{left:393px;top:490px;width:140px;height:140px;border-radius:50%;background:var(--orange-deep);border:8px solid var(--grey-light);color:var(--white);text-align:center;font-weight:700}
  .offer .save{position:absolute;right:20px;top:12px;font-style:italic;font-weight:400;font-size:14px}
  .offer .amount{position:absolute;left:0;right:0;top:16px;font-size:58px;line-height:1}
  .offer .amount sup{font-size:18px;font-weight:400;vertical-align:top;position:relative;top:8px}
  .offer .terms{position:absolute;left:0;right:0;top:86px;font-size:13px;line-height:1.05}
  .tagline{left:128px;top:676px;color:var(--white);font-style:italic}
  .tagline .a{font-size:22px;font-weight:300;position:absolute;left:0;top:38px}
  .tagline .breeze{font-size:78px;font-weight:900;position:absolute;left:30px;top:0;line-height:1}
  .tagline .without{font-size:21px;font-weight:300;position:absolute;left:80px;top:70px;white-space:nowrap}
  .tagline .cost{font-size:78px;font-weight:900;position:absolute;left:198px;top:54px;line-height:1}

  /* back */
  .intro{left:0;right:0;top:14px;text-align:center;color:var(--white);font-weight:700;font-style:italic;font-size:15.5px;line-height:1.4}
  .reviews{left:30px;top:126px;width:420px;color:var(--white);font-size:11.5px;line-height:1.15}
  .review{margin-bottom:14px}
  .review q{quotes:"\201C" "\201D"}
  .review q::before,.review q::after{font-size:18px;font-weight:700;vertical-align:-3px}
  .review cite{display:block;font-style:italic;font-weight:700;font-size:11px}
  .promise-heading{left:45px;top:225px;color:var(--white);font-size:19px;font-weight:700;font-style:italic}
  .guarantee{left:45px;top:270px;width:492px;height:312px;background:linear-gradient(180deg,#fff 0%,#eef0f1 100%);border-radius:8px;box-shadow:0 4px 10px rgba(0,0,0,.25)}
  .guarantee h3{position:absolute;left:82px;top:36px;font-size:16px;font-weight:700;font-style:italic;color:#555}
  .guarantee ul{position:absolute;left:85px;top:70px;list-style:none;font-size:10.6px;color:#444;line-height:20.8px}
  .guarantee li::before{content:"• "}
  .guarantee b{font-weight:700}
  .back-brand{left:420px;top:470px;width:130px}
  .pill{position:absolute;top:648px;height:68px;background:var(--grey);color:var(--white)}
  .pill--phone{left:0;width:216px;border-radius:0 30px 0 0}
  .pill--phone span{position:absolute;left:40px;top:20px;font-size:23px;font-style:italic;font-weight:400}
  .pill--pay{left:364px;width:217px;border-radius:30px 0 0 0;text-align:center}
  .pill--pay .label{display:block;margin-top:12px;font-size:15px;font-weight:700}
  .cards{display:flex;gap:10px;justify-content:center;margin-top:6px}
  .cards i{width:34px;height:20px;background:var(--white);border:1px solid #ddd}
  .web{left:0;right:0;top:734px;text-align:center;color:var(--white);font-weight:700;font-size:15px}
  .conditions{right:48px;top:782px;text-align:right;color:var(--white)}
  .conditions h4{font-size:15px;font-weight:700}
  .conditions p{font-size:9px;margin-top:3px;white-space:nowrap}
</style>
</head>
<body>
<main class="canvas">

  <section class="page page--front">
    <svg class="shapes" width="581" height="824" viewBox="0 0 581 824">
      <polygon points="0,150 581,130 581,640 0,720" fill="#d9d6d0" role="img" aria-label="Photo of a woman leaping through a bright room beneath a ceiling fan"/>
      <polygon points="60,110 330,150 340,200 80,240" fill="var(--orange-deep)"/>
      <polygon points="0,0 520,0 581,40 560,220 380,210 110,260 0,200" fill="var(--teal)"/>
      <polygon points="480,0 581,0 581,190 540,220" fill="var(--teal-dark)"/>
      <polygon points="50,690 310,640 340,660 70,720" fill="var(--orange-deep)"/>
      <polygon points="0,700 340,650 581,600 581,824 0,824" fill="var(--teal)"/>
      <polygon points="0,640 60,690 0,760" fill="var(--teal-dark)"/>
    </svg>
    <h1 class="abs front-title"><span class="light">Hot Sweaty</span><span class="bold">Uncomfortable</span></h1>
    <div class="abs brand front-brand"><span class="dot"></span>Spark Ready Electrical</div>
    <div class="abs offer">
      <span class="save">Save</span>
      <span class="amount"><sup>$</sup>25</span>
      <span class="terms">OFF EVERY 2<sup style="font-size:8px">ND</sup><br>FAN INSTALLED</span>
    </div>
    <p class="abs tagline">
      <span class="a">A</span><span class="breeze">breeze</span>
      <span class="without">without the</span><span class="cost">cost!</span>
    </p>
  </section>

  <section class="page page--back">
    <svg class="shapes" width="581" height="824" viewBox="0 0 581 824">
      <defs>
        <linearGradient id="bandOrange" x1="0" x2="1">
          <stop offset="0" stop-color="var(--orange)"/><stop offset="1" stop-color="var(--orange-soft)"/>
        </linearGradient>
      </defs>
      <rect x="0" y="0" width="581" height="70" fill="url(#bandOrange)"/>
      <rect x="0" y="70" width="581" height="12" fill="#f7c98a"/>
      <polygon points="210,280 420,250 470,150 455,145 530,110 510,190 495,175 440,270 240,305" fill="var(--orange)"/>
      <polygon points="10,360 70,340 60,440" fill="var(--orange)"/>
      <polygon points="100,610 210,530 420,570 300,590" fill="var(--orange)"/>
      <path d="M0,824 L0,790 Q80,760 300,762 L581,762 L581,824 Z" fill="url(#bandOrange)"/>
      <path d="M20,690 Q10,640 40,628 L50,650 Q35,660 40,690 Q45,720 60,730 L50,752 Q25,740 20,690 Z" fill="var(--orange)"/>
    </svg>
    <p class="abs intro">Enjoy the gentle breeze &amp; cooling effect of a ceiling fan to help you<br>sleep soundly at night &amp; be more productive during the day.</p>
    <div class="abs reviews">
      <blockquote class="review"><q>We can now sleep! Wow what a difference! Thanks Daniel for your help.</q><cite>OLIVER &amp; GRACE WHITFIELD</cite></blockquote>
      <blockquote class="review"><q>Super service! What a pleasant change. Daniel could not have done more to ensure our satisfaction.</q><cite>SAM &amp; LUCIA</cite></blockquote>
    </div>
    <h2 class="abs promise-heading">Our Promise To You:</h2>
    <div class="abs guarantee">
      <h3>We guarantee to</h3>
      <ul>
        <li><b>Always be on time</b>, or we pay you <b>$100</b></li>
        <li>Tell you the <b>exact cost</b> before any <b>job begins</b></li>
        <li>Provide you with a <b>fixed price guarantee</b>, assuring you have <b>no extra costs</b></li>
        <li>Leave your place as <b>clean</b> as it was when we <b>first arrived</b></li>
        <li>Return, and <b>fix it for free</b>, if its not right</li>
        <li>Return your telephone <b>calls promptly</b></li>
        <li>Provide a minimum <b>12 Month</b> warranty on all parts</li>
        <li>Provide friendly, <b>helpful service and advice</b></li>
      </ul>
    </div>
    <div class="abs brand back-brand"><span class="dot"></span>Spark Ready Electrical</div>
    <div class="pill pill--phone"><span>1300 482 617</span></div>
    <div class="pill pill--pay"><span class="label">Digital Payment</span><div class="cards"><i></i><i></i><i></i></div></div>
    <p class="abs web">www.sparkreadyelectrical.com.au</p>
    <div class="abs conditions">
      <h4>Conditions:</h4>
      <p>Mention this ad when booking to receive offer. Limit one per household. Cannot be combined with any other offer.</p>
    </div>
  </section>

</main>
</body>
</html>
```